UK garage/funky house night flier

I need a flier design to upload to my sociallink event page and also some printed fliers to promote the event.

Event is in an urban area underneath railway arches so would like a flier to reflect this with an urban background.

new photos uploaded to be used as possible backgrounds

Target Market(s)

aged 18-30

Industry/Entity Type

House

Requirements
Must have
• The following text on front of flier:

TRUE PULSE ENTERTAINMENTS PRESENTS A NIGHT CALLED…

‘MIDNIGHT CELLAR RHYTHMZ’

Saturday 7th September 2013

@ Dock47, Harlow Lane, Digbeth, Birmingham B9 3QW

9pm till late

DJ’s playing a selection of Funky house/deep house/future garage and old school 2-step garage

(On back of flier......)

Come and enjoy yourself in a friendly, safe environment with like-minded people who are out to have a good time and rave till the early hours. This venue is part outdoor terrace and part indoor with music being played on the Wavecraft Soundsystem – so you know it is a night not to be missed!!

This event is guestlist only. Those not on the guest list will not be allowed entry. To get yourself on the guest list go to the sociallink page www.sociallink.example/truepulseentertainments and join the event ‘Midnight Cellar Rhythmz’

Dresscode: smart. No trainers/tracksuits
Admission fee on the door is £5
Last entry: midnight
Nice to have
• must be portrait, A5 or A6 size

Urban background, maybe at night, a street with old brickwork, maybe some speakers in the foreground.

dock47 logo bottom right

Back of flier to have the map of Dock47

```html
<!DOCTYPE html>
<html lang="en">
<head>
<meta charset="utf-8">
<title>Midnight Cellar Rhythmz – Flier</title>
<link rel="stylesheet" href="https://fonts.googleapis.com/css2?family=Gochi+Hand&family=Rubik+Distressed&display=swap">
<style>
  :root {
    --stage-top: #ccd6d3;
    --stage-bottom: #a8b4b2;
    --lime: #e4f23a;
    --lime-glow: #d6f02c;
    --title-blue: #4ea6ea;
    --night: #05060c;
    --arch-violet: #4a3a78;
    --arch-light: #c9d6ee;
    --magenta: #d94cf0;
    --white: #f4f4f4;
    --glow-blue: #1f49c8;
    --hand: "Gochi Hand", cursive;
  }
  * { margin: 0; padding: 0; box-sizing: border-box; }
  html, body { width: 1200px; height: 1000px; overflow: hidden; }
  body {
    position: relative;
    background: radial-gradient(ellipse at 50% 45%, var(--stage-top), var(--stage-bottom));
    font-family: var(--hand);
  }
  .flier {
    position: absolute;
    overflow: hidden;
    background: var(--night);
    box-shadow: 0 4px 14px rgba(0,0,0,.35);
    text-align: center;
  }
  .flier p, .flier h1, .flier div { font-family: var(--hand); }

  /* front */
  .flier--front { left: 77px; top: 110px; width: 511px; height: 725px; }
  .arch-photo {
    position: absolute; inset: 0;
    background:
      radial-gradient(ellipse 40% 35% at 45% 43%, var(--arch-light), rgba(120,130,200,.6) 45%, transparent 80%),
      linear-gradient(180deg, #0a0a18 0%, var(--arch-violet) 40%, #1a1840 70%, #06060e 100%);
  }
  .front__intro {
    position: absolute; top: 26px; left: 0; right: 0;
    font-size: 25px; line-height: 27px; letter-spacing: 2.5px;
    color: var(--lime); text-transform: uppercase;
  }
  .flier .front__title {
    position: absolute; top: 138px; left: 0; right: 0;
    font-family: "Rubik Distressed", cursive;
    font-weight: 400;
    font-size: 70px; line-height: 94px;
    color: var(--title-blue);
    text-shadow: 0 0 3px var(--lime-glow), 0 0 6px var(--lime-glow), 0 0 10px var(--lime-glow), 0 0 2px var(--lime-glow);
  }
  .front__date { position: absolute; top: 460px; left: 0; right: 0; font-size: 23px; color: var(--lime); }
  .front__venue { position: absolute; top: 492px; left: 0; right: 0; font-size: 16px; line-height: 22px; color: var(--white); }
  .front__lineup { position: absolute; top: 553px; left: 0; right: 0; font-size: 20px; line-height: 28px; letter-spacing: 1px; color: var(--lime); }
  .venue-mark {
    position: absolute; left: 374px; top: 656px; width: 96px; height: 30px;
    display: flex; align-items: center; justify-content: center; gap: 6px;
    background: var(--white);
    font-size: 16px; color: #333a44;
  }
  .venue-mark__square { width: 9px; height: 9px; background: #333a44; }

  /* back */
  .flier--back { left: 637px; top: 110px; width: 508px; height: 720px; }
  .back__glow {
    position: absolute; left: 240px; top: 430px; width: 320px; height: 320px;
    border-radius: 50%;
    background: radial-gradient(circle, rgba(31,73,200,.85) 0%, rgba(31,73,200,.55) 45%, rgba(31,73,200,0) 72%);
  }
  .back__map {
    position: absolute; left: 46px; top: 47px; width: 418px; height: 276px;
    background: linear-gradient(135deg, #ffffff, #e6e8ea);
    border: 2px solid #d0d0d0;
  }
  .back__copy { position: absolute; left: 24px; right: 24px; }
  .back__about { top: 336px; font-size: 16px; line-height: 21px; color: var(--lime); }
  .back__hype { top: 425px; font-size: 20px; color: var(--magenta); letter-spacing: .5px; }
  .back__guestlist { top: 461px; font-size: 18px; line-height: 19px; color: var(--lime); letter-spacing: .6px; text-shadow: 0 0 .6px var(--lime); }
  .back__guestlist u { text-decoration-color: var(--magenta); }
  .flier .back__link { top: 537px; font-family: Georgia, serif; font-style: italic; font-size: 14px; line-height: 24px; color: var(--magenta); }
  .back__details { top: 594px; font-size: 21px; line-height: 29px; letter-spacing: 1px; color: var(--lime); }
</style>
</head>
<body>
  <section class="flier flier--front">
    <div class="arch-photo" role="img" aria-label="Night photo of an old brick railway arch tunnel lit with blue and violet light"></div>
    <p class="front__intro">True Pulse Entertainments<br>presents<br>a night called…</p>
    <h1 class="front__title">MIDNIGHT<br>CELLAR<br>RHYTHMZ</h1>
    <p class="front__date">Saturday 7th September 2013</p>
    <p class="front__venue">@ Dock47, Harlow Lane, Digbeth, Birmingham B9 3QW<br>9pm till late</p>
    <p class="front__lineup">DJ’s playing a selection of<br>Funky house/deep house/future garage<br>and old school 2-step garage</p>
    <div class="venue-mark"><span class="venue-mark__square"></span>DOCK47</div>
  </section>

  <section class="flier flier--back">
    <div class="back__glow" role="img" aria-label="Blue music graphic in the lower right corner"></div>
    <div class="back__map" role="img" aria-label="Street map of Digbeth showing the route to Dock47"></div>
    <p class="back__copy back__about">Come and enjoy yourself in a friendly, safe environment with like-minded people who are out to have a good time and rave till the early hours. This venue is part outdoor terrace and part indoor with music being played on the Wavecraft Soundsystem</p>
    <p class="back__copy back__hype">so you know it is a night not to be missed!</p>
    <p class="back__copy back__guestlist">This event is <u>guestlist only</u>. Those not on the guest list will not be allowed entry. To get yourself on the guest list go to the sociallink.</p>
    <p class="back__copy back__link">www.sociallink.example/truepulseentertainments<br>and join the event ‘Midnight Cellar Rhythmz’</p>
    <p class="back__copy back__details">Dresscode: smart. No trainers/tracksuits<br>Admission fee on the door is £5<br>Last entry: midnight</p>
  </section>
</body>
</html>
```